Business Card Design

We offer full auto repair and auto customization from custom wheels to lift kits and drop kits we do it all. I want something that grabs your attention from the start but nothing flashy i am more of a clean crisp modern kinda of guy. I plan on using the design on my business cards and my main business sign .
Updates
I have up loaded an image of my currant business card designed by me , I would like to improve on it
Target Market(s)
20-35 male and female
Industry/Entity Type
Business
Contact Information for Business Card
Corvello Wheel Works
48362 1/2 Parkfield rd
Houston TX, 77070
Manager: Dorian Walsh
P:555-214-7730
F:555-214-7781
Email:Dorian@corvellowheelandgarage.example
website:Corvellowheelandgarage.example
Look and feel

```html
<!DOCTYPE html>
<html lang="en">
<head>
<meta charset="utf-8">
<title>Corvello Wheel Works – Business Card</title>
<link rel="stylesheet" href="https://fonts.googleapis.com/css2?family=Tenor+Sans&family=Arimo:wght@400&display=swap">
<style>
  :root {
    --blue-deep: #0a4c7a;
    --blue-mid: #2a86bf;
    --blue-light: #6cc0e6;
    --brand-blue: #064f80;
    --ink-dark: #3a3a48;
    --ink-blue: #1b5e8e;
    --bullet: #3a8fc8;
    --white: #ffffff;
  }
  * { margin: 0; padding: 0; box-sizing: border-box; }
  html, body { width: 1052px; height: 1200px; overflow: hidden; background: var(--white); }
  .canvas { position: relative; width: 1052px; height: 1200px; }

  .brand-square { position: absolute; background: var(--brand-blue); }
  .brand-name {
    position: absolute;
    font-family: "Tenor Sans", sans-serif;
    font-weight: 400;
    letter-spacing: 2px;
    white-space: nowrap;
  }

  .card-front {
    position: absolute; left: 0; top: 0; width: 1052px; height: 601px;
    background: radial-gradient(ellipse 60% 70% at 50% 48%, var(--blue-light) 0%, var(--blue-mid) 50%, var(--blue-deep) 100%);
  }
  .card-front .brand-square { left: 428px; top: 172px; width: 196px; height: 196px; }
  .card-front .brand-name {
    left: 0; width: 1052px; text-align: center; top: 392px;
    font-size: 40px; color: var(--ink-dark);
  }

  .card-back { position: absolute; left: 0; top: 601px; width: 1052px; height: 599px; background: var(--white); }
  .card-back .brand-square { left: 246px; top: 112px; width: 176px; height: 176px; }
  .card-back .brand-name { left: 113px; top: 306px; font-size: 36px; color: var(--ink-dark); }

  .person {
    position: absolute; right: 38px; top: 64px; text-align: right;
    font-family: "Tenor Sans", sans-serif; color: var(--ink-blue);
  }
  .person-name { font-size: 44px; line-height: 1; }
  .person-title { font-size: 27px; line-height: 1.2; margin-top: 2px; }

  .services {
    position: absolute; left: 698px; top: 318px; width: 310px; list-style: none;
    font-family: "Tenor Sans", sans-serif; color: var(--ink-dark);
  }
  .services li {
    position: relative; height: 29px; font-size: 24px; line-height: 29px;
    text-align: right; letter-spacing: 0.5px; -webkit-text-stroke: 0.6px var(--ink-dark);
  }
  .services li::before {
    content: ""; position: absolute; left: 0; top: 7px; width: 17px; height: 17px; border-radius: 50%;
    background: radial-gradient(circle at 35% 35%, #bfe4f7 0%, var(--bullet) 55%, #1a5f93 100%);
  }

  .contact-bar {
    position: absolute; left: 0; top: 472px; width: 1052px; height: 42px;
    background: linear-gradient(90deg, var(--blue-deep) 0%, #2e8cc5 45%, #4aa6d8 60%, var(--blue-deep) 100%);
    display: flex; align-items: center; justify-content: center; gap: 14px;
    font-family: "Arimo", sans-serif; font-size: 17px; color: var(--white); white-space: nowrap;
  }
  .address {
    position: absolute; left: 0; width: 1052px; top: 536px; text-align: center;
    font-family: "Arimo", sans-serif; font-size: 25px; color: var(--ink-blue);
  }
</style>
</head>
<body>
  <div class="canvas">
    <section class="card-front">
      <div class="brand-square"></div>
      <div class="brand-name">Corvello Wheel Works</div>
    </section>

    <section class="card-back">
      <div class="person">
        <div class="person-name">Dorian Walsh</div>
        <div class="person-title">Manager</div>
      </div>

      <div class="brand-square"></div>
      <div class="brand-name">Corvello Wheel Works</div>

      <ul class="services">
        <li>New and Used Tires</li>
        <li>Custom Wheels</li>
        <li>Tire Repair</li>
        <li>Shocks</li>
        <li>Brakes</li>
      </ul>

      <div class="contact-bar">
        <span class="tel">Tel : 555-214-7730</span>
        <span class="fax">Fax : 555-214-7781</span>
        <span class="web">www.Corvellowheelandgarage.example</span>
        <span class="email">Dorian@corvellowheelandgarage.example</span>
      </div>

      <div class="address">48362 1/2 Parkfield Rd Houston, TX 77070</div>
    </section>
  </div>
</body>
</html>
```